Counseling Practice Business Card

I need a professional looking business card incorporating my new logo that was just completed. Card needs to incorporate my name and title, description of my specialty, my address, my phone number, my fax number, my email and my website URL. I need to be able to choose design on/with different paper colors and textures.
I do not have a lot of business card ideas so I am open to anything but I want bold,sharp, clear card without additional designs other than my logo (see attached file info). I am open to different color backgrounds or paper colors including black. I do not like traditional brackets around area codes in phone number or dashes between numbers in phone number. Am open to other ways of presenting including periods between numbers as appropriate. I do not know enough to know what I like yet but I want card to coordinate and work together with my logo. My practice emphasizes natural mental health interventions so any use of color (with background paper color or the blue and green in my logo) that elicits nature is nice. In addition to black, any natural brown or wood looking background might be desirable also. Most of the offerings so far look very similar and boring.

Target Market(s)

Potential therapy clients and other professionals

Contact Information for Business Card

Card information:
Marcus T. Whitfield, Ph.D.
Licensed Clinical Psychologist
Integrative Health Coach
4812 Ferndale Pkwy NW
Suite 730
Brookvale, GA 30421
(470) 555-0142 phone
(470) 555-0186 fax
drmarcuswhitfield@kelvora.com
pathbloomcounseling.com

Font styles to use
Serif
Sans Serif
Other font styles liked:
• anything that you think looks crisp, clear and easily readable

Requirements
Must have
• Any color used should coordinate with my logo design (see attached files).
• Card should be printed horizontally so top and bottom are longest sides of rectangle.
• Background color or paper color should complement and highlight logo. Do not like a white background. black, grey, brown or any color my logo would blend well with.
Nice to have
• I would like designer to utilize color to highlight letters/name or phone-fax-web symbols.
• Bottom edge of card could be highlighted if appropriate to an idea.
Should not have
• I would NOT want the card to have a pure white background at all.
• No clear cards.
• Cards should be oriented with long sides on bottom and top, NOT sides. DO NOT LIKE THIS THIN TALL ORIENTATION.

```html
<!DOCTYPE html>
<html lang="en">
<head>
<meta charset="utf-8">
<title>Pathbloom Counseling – Business Card</title>
<link rel="stylesheet" href="https://fonts.googleapis.com/css2?family=Montserrat:wght@300;400;500;600&display=swap">
<style>
  :root {
    --page: #ffffff;
    --card: #232323;
    --blue: #2372b6;
    --green: #17652f;
    --white: #f2f2f2;
  }
  html, body {
    margin: 0;
    padding: 0;
    width: 1200px;
    height: 1200px;
    overflow: hidden;
    background: var(--page);
    font-family: "Montserrat", sans-serif;
  }
  .card {
    position: absolute;
    left: 138px;
    top: 80px;
    width: 926px;
    height: 530px;
    background: var(--card);
  }
  .brand {
    position: absolute;
    left: 62px;
    top: 224px;
    width: 300px;
    display: flex;
    align-items: center;
    gap: 12px;
    color: var(--blue);
    font-weight: 500;
  }
  .brand-dot {
    width: 22px;
    height: 22px;
    border-radius: 50%;
    background: var(--blue);
    flex: none;
  }
  .brand-name {
    font-size: 44px;
    line-height: 1;
    letter-spacing: -0.5px;
  }
  .brand-sub {
    display: block;
    font-size: 15px;
    letter-spacing: 9px;
    margin-top: 10px;
  }
  .details {
    position: absolute;
    left: 420px;
    top: 88px;
    color: var(--white);
  }
  .name {
    margin: 0;
    font-size: 32px;
    line-height: 44px;
    font-weight: 600;
    color: var(--blue);
    letter-spacing: 0.4px;
  }
  .titles {
    margin: 2px 0 0;
    font-size: 22.5px;
    font-weight: 300;
    color: var(--green);
    line-height: 30px;
    letter-spacing: 0.7px;
  }
  .address {
    margin: 8px 0 0;
    font-size: 23px;
    font-weight: 400;
    line-height: 27px;
    letter-spacing: 0.7px;
  }
  .contacts {
    list-style: none;
    margin: 22px 0 0 -4px;
    padding: 0;
  }
  .contacts li {
    display: flex;
    align-items: center;
    gap: 10px;
    height: 42px;
    font-size: 23px;
    letter-spacing: 0.7px;
  }
  .contacts svg {
    width: 28px;
    height: 28px;
    fill: var(--blue);
    flex: none;
  }
</style>
</head>
<body>
  <section class="card">
    <div class="brand">
      <span class="brand-dot"></span>
      <div>
        <span class="brand-name">Pathbloom</span>
        <span class="brand-sub">COUNSELING</span>
      </div>
    </div>

    <div class="details">
      <h1 class="name">Marcus T. Whitfield, Ph.D.</h1>
      <p class="titles">Licensed Clinical Psychologist<br>Integrative Health Coach</p>
      <p class="address">4812 Ferndale Pkwy NW<br>Suite 730 Brookvale, GA 30421</p>
      <ul class="contacts">
        <li>
          <svg viewBox="0 0 28 28" aria-label="Fax"><rect x="8" y="2" width="12" height="8"/><rect x="2" y="10" width="24" height="16" rx="2"/><rect x="9" y="15" width="12" height="9" fill="#232323"/><rect x="11" y="17" width="8" height="1.5"/><rect x="11" y="20" width="8" height="1.5"/></svg>
          (470) 555-0186
        </li>
        <li>
          <svg viewBox="0 0 28 28" aria-label="Phone"><path d="M9 2c1 0 2 1 2 2l1 5c0 1-1 2-2 2 0 3 3 8 6 10 1-1 2-1 3 0l4 3c1 1 0 2-1 3-2 1-5 1-8-2C8 20 5 13 5 8c0-3 2-6 4-6z"/></svg>
          (470) 555-0142
        </li>
        <li>
          <svg viewBox="0 0 28 28" aria-label="Email"><path d="M1 6h26v17H1z"/><path d="M1 6l13 10L27 6" fill="none" stroke="#232323" stroke-width="2"/></svg>
          drmarcuswhitfield@kelvora.com
        </li>
        <li>
          <svg viewBox="0 0 28 28" aria-label="Website"><g fill="none" stroke="#2372b6" stroke-width="2"><circle cx="14" cy="14" r="12"/><ellipse cx="14" cy="14" rx="5" ry="12"/><path d="M2 14h24M4 8h20M4 20h20M14 2v24"/></g></svg>
          pathbloomcounseling.com
        </li>
      </ul>
    </div>
  </section>
</body>
</html>
```